Stationery design for pet company

We need a designer for stationery designs. The name of our company is Plimarv. We specialise in pet accessories as well as distribution of pet food. We also have a brand under us for our website called Tailwaggroove. We will need a letterhead for Plimarv and another for Tailwaggroove with matching envelopes. We also would like to have a business card design with name, contact details etc with the Plimarv logo on one side of the card. The other side of the business card should have the full logo of Tailwaggroove with our website www.tailwaggroove.example.

Target Market(s)

Stationery for Plimarv is for retail shops and suppliers, therefore should have a more professional feel. Stationery for Tailwaggroove is mainly for customers from the website.

Industry/Entity Type

Business

Requirements
Must have
• Preferably a use of black colour for the business card.
Nice to have
• Professional feel
Should not have
• Childish designs

```html
<!DOCTYPE html>
<html lang="en">
<head>
<meta charset="utf-8">
<title>Plimarv Letterhead</title>
<link href="https://fonts.googleapis.com/css2?family=Tinos:wght@400;700&display=swap" rel="stylesheet">
<style>
  :root {
    --paper: #ffffff;
    --ink: #111111;
    --brand-dark: #1f2a44;
    --brand-gold: #c59a3e;
    --footer-gold: #c9a456;
    --rule: #555555;
    --watermark: #f8f4ec;
  }
  html, body {
    margin: 0;
    padding: 0;
    overflow: hidden;
    background: var(--paper);
  }
  .letterhead {
    position: relative;
    width: 835px;
    height: 1200px;
    background: var(--paper);
    font-family: "Tinos", "Times New Roman", serif;
    color: var(--ink);
    overflow: hidden;
  }
  .brand {
    position: absolute;
    left: 22px;
    top: 40px;
    display: flex;
    align-items: center;
    gap: 14px;
  }
  .brand-dot {
    width: 44px;
    height: 44px;
    border-radius: 50%;
    background: var(--brand-gold);
  }
  .brand-name {
    font-size: 46px;
    font-weight: 700;
    letter-spacing: 3px;
    color: var(--brand-dark);
    line-height: 1;
  }
  .sender {
    position: absolute;
    right: 12px;
    top: 12px;
    text-align: right;
    font-size: 18px;
    line-height: 1.12;
  }
  .sender-name {
    font-size: 26px;
    font-weight: 700;
    margin-bottom: 2px;
  }
  .header-rule,
  .footer-rule {
    position: absolute;
    left: 0;
    width: 835px;
    height: 0;
    border-top: 1.5px solid var(--rule);
  }
  .header-rule { top: 153px; }
  .footer-rule { top: 1156px; }
  .watermark {
    position: absolute;
    left: 150px;
    top: 330px;
    width: 530px;
    height: 530px;
    border-radius: 50%;
    background: var(--watermark);
  }
  .footer-contact {
    position: absolute;
    left: 0;
    width: 835px;
    top: 1168px;
    text-align: center;
    font-size: 22px;
    color: var(--footer-gold);
  }
</style>
</head>
<body>
  <div class="letterhead">
    <div class="brand">
      <span class="brand-dot"></span>
      <span class="brand-name">PLIMARV</span>
    </div>

    <div class="sender">
      <div class="sender-name">Plimarv</div>
      <div>Address line1</div>
      <div>Address line2,</div>
      <div>Address line 3</div>
      <div>Phone: (123) 123 123 123</div>
    </div>

    <div class="header-rule"></div>

    <div class="watermark" role="img" aria-label="Faint brand emblem background"></div>

    <div class="footer-rule"></div>
    <div class="footer-contact">Email: email@email.com Website: www.tailwaggroove.example</div>
  </div>
</body>
</html>
```